Web Design Project for Industrial Hemp

I'm launching a new company to grow Industrial Hemp and then to set up a manufacturing facility to process the crop each and every year. We require a complete end to end brand and livery suite and we will start with a web presence. We want to appeal to (a) Investors, Employees, Farmers, and consumers so as to engage with all our stakeholders. We want to create a whole new industry that becomes a game changer for environmentally friendly crop production. Hemp is gaining in popularity and credibility across the world!

Target Market(s)

Farmers to produce, Manufacturers who will purchase the raw materials, Investors who will invest in the project, Consumers who will buy Hemp Products

Industry/Entity Type

Industry

Requirements
Must have
• Environmentally Friendly
Carbon Neutral/Positive
Game Changer
Multi-Use Crop
50,000 products can be made from Hemp
Should not have
• Should avoid its relationship with cannabis but not ignore it! When the regulatory bodies acknowledge the benefits of cannabanoids, they will start to legalise the production of cannabis for sale on prescription

```html
<!DOCTYPE html>
<html lang="en">
<head>
<meta charset="utf-8">
<title>Verdant Stem &amp; Seed</title>
<link href="https://fonts.googleapis.com/css2?family=Arimo:wght@400;700&display=swap" rel="stylesheet">
<style>
:root{
  --page:#f1f0eb;
  --panel:#ffffff;
  --green:#4f8a1c;
  --green-dark:#3f7414;
  --green-text:#3d7a0c;
  --red:#b0141b;
  --text:#4a4a4a;
  --muted:#666;
  --rule:#d9d9d9;
}
*{box-sizing:border-box;margin:0;padding:0}
html,body{width:1104px;height:1200px;overflow:hidden}
body{background:var(--page);font-family:'Arimo',Arial,sans-serif;color:var(--text);position:relative}
.brand{position:absolute;left:83px;top:26px;font-size:36px;font-weight:700;color:var(--red);letter-spacing:-.3px}
.search{position:absolute;left:828px;top:28px;width:192px;height:32px;background:#fff;border:1px solid #d4d4d4;font-size:11px;color:#777;padding:11px 0 0 13px}
.search svg{position:absolute;right:9px;top:8px}
.nav{position:absolute;left:83px;top:86px;width:937px;height:50px;background:linear-gradient(#5c9a22,var(--green-dark));border-radius:3px 3px 0 0;display:flex;align-items:stretch}
.nav a{color:#fff;text-decoration:none;font-size:14px;display:flex;align-items:center;justify-content:center;border-right:1px solid #3a6a12}
.nav a.active{background:linear-gradient(#5a5a5a,#333)}
.nav .call{margin-left:auto;color:#fff;font-weight:700;font-size:18px;display:flex;align-items:center;padding-right:17px}
.panel{position:absolute;left:83px;top:136px;width:937px;height:980px;background:var(--panel)}
.hero{position:absolute;left:8px;top:7px;width:925px;height:344px;background:linear-gradient(180deg,#5c93c9 0%,#a9c8e3 30%,#8a8f6a 42%,#2f6c99 50%,#3d6f8d 60%,#9b7040 75%,#b07034 100%)}
.hero .arrow{position:absolute;top:163px;width:32px;height:32px;border-radius:50%;background:rgba(255,255,255,.85)}
.hero .caption{position:absolute;left:22px;top:258px;color:#fff;font-weight:700;font-size:25px;line-height:32px;text-shadow:1px 2px 3px rgba(0,0,0,.6)}
.main{position:absolute;left:10px;top:382px;width:646px}
h1,h2,h3{color:var(--red);font-weight:700}
h1{font-size:21px;margin-bottom:14px}
h2{font-size:17px;margin-bottom:15px}
p{font-size:12px;line-height:21px;text-align:justify;margin-bottom:8px}
hr{border:0;border-top:1px solid var(--rule);margin:14px 0 23px}
.uses{display:grid;grid-template-columns:207px 236px 1fr;margin-top:14px}
.use{padding:0 0 14px 0;position:relative}
.use h3{font-size:14px;font-weight:400;margin-bottom:6px}
.use p{color:var(--green-text);font-size:12px;line-height:16px;text-align:left;margin:0;width:186px}
.use.sep{border-left:1px solid var(--rule);padding-left:28px}
.use.top::after{content:"";position:absolute;left:0;right:26px;bottom:0;border-bottom:1px solid var(--rule)}
.use.sep.top::after{left:28px;right:20px}
.use.bottom{padding-top:14px}
.contact-head{position:absolute;left:695px;top:379px;height:30px;display:flex;align-items:center;gap:9px}
.contact-head h2{margin:0}
.contact{position:absolute;left:682px;top:421px;width:240px;height:424px;background:linear-gradient(var(--green),var(--green-dark));border-radius:3px;padding:16px}
.contact label{display:block;color:#fff;font-size:12px;line-height:14px;margin-bottom:4px}
.contact .field{height:33px;background:#fff;border:1px solid #ccc;margin-bottom:22px}
.contact .field.msg{height:128px;margin-bottom:14px}
.contact .submit{float:right;height:30px;line-height:30px;background:linear-gradient(#555,#2d2d2d);color:#fff;font-weight:700;font-size:14px;padding:0 12px;border-radius:3px}
.news{position:absolute;left:8px;top:877px;width:922px;height:94px;background:#efefef;border:1px solid #ddd;border-radius:2px}
.news .label{position:absolute;left:24px;top:31px;display:flex;align-items:center;gap:20px}
.news h2{margin:0;font-size:17px}
.news p{position:absolute;left:237px;top:16px;width:600px;margin:0;font-size:12px}
.news .date{color:var(--green-text)}
.news .next{position:absolute;right:18px;top:35px}
.footer-links{position:absolute;left:83px;top:1134px;font-size:13px;color:#555;word-spacing:2px}
.copyright{position:absolute;left:83px;top:1163px;font-size:13px;color:#555}
.social{position:absolute;left:970px;top:1147px;display:flex;gap:4px}
.social span{width:22px;height:22px;border-radius:3px;display:block}
</style>
</head>
<body>
<div class="brand">Verdant Stem &amp; Seed</div>
<div class="search">Search
  <svg width="16" height="16" viewBox="0 0 16 16"><circle cx="6" cy="6" r="4.5" fill="none" stroke="#333" stroke-width="2"/><line x1="9.5" y1="9.5" x2="14" y2="14" stroke="#333" stroke-width="3"/></svg>
</div>
<nav class="nav">
  <a class="active" style="width:84px">Home</a>
  <a style="width:98px">About us</a>
  <a style="width:97px">Services</a>
  <a style="width:98px">Products</a>
  <a style="width:77px">News</a>
  <a style="width:106px">Contact us</a>
  <div class="call">Call us : 555 010 2244</div>
</nav>
<div class="panel">
  <div class="hero" role="img" aria-label="Landscape photo of hills, a blue bay and a coastal town under a bright sky">
    <svg class="arrow" style="left:22px" viewBox="0 0 32 32"><path d="M18 10l-6 6 6 6" fill="none" stroke="#888" stroke-width="1.5"/></svg>
    <svg class="arrow" style="right:22px" viewBox="0 0 32 32"><path d="M14 10l6 6-6 6" fill="none" stroke="#888" stroke-width="1.5"/></svg>
    <div class="caption">Environmentally Friendly<br>50,000 products can be made from Hemp</div>
  </div>
  <div class="main">
    <h1>Welcome to Verdant Stem &amp; Seed</h1>
    <p>Sed fringilla, libero id placerat accumsan, velit est condimentum neque, id vestibulum nibh dolor eu urna. Suspendisse sollicitudin tristique dui, ac pellentesque erat accumsan ut. Vivamus tellus enim, adipiscing id massa vestibulum, placerat porttitor justo. Duis posuere eget risus vel condimentum. Duis condimentum ipsum in leo pulvinar porta. Aliquam blandit sem ut ultricies hendrerit. Praesent tristique augue sit amet ligula blandit, facilisis facilisis augue placerat. Vestibulum ante ipsum primis in faucibus orci luctus et ultrices posuere cubilia Curae.</p>
    <p>Sed vel facilisis sapien, nec mollis erat. Donec malesuada ligula sit amet mi faucibus sollicitudin. Phasellus scelerisque lorem sem. Praesent rhoncus eget augue quis facilisis.</p>
    <hr>
    <h2>Got Hemp?</h2>
    <p>Donec quis convallis diam. Sed commodo ipsum quam, a elementum nisl rutrum vitae. Ut vehicula nisl sem, eu congue mauris tempor ac. In congue, turpis vel congue eleifend, diam magna placerat nisi.</p>
    <div class="uses">
      <div class="use top"><h3>Food</h3><p>Donec quam lacus, imperdiet at vehicula at, bibendum.</p></div>
      <div class="use sep top"><h3>Fuel</h3><p>Donec quam lacus, imperdiet at vehicula at, bibendum.</p></div>
      <div class="use sep top"><h3>Fiber</h3><p>Donec quam lacus, imperdiet at vehicula at, bibendum.</p></div>
      <div class="use bottom"><h3>Oil</h3><p>Donec quam lacus, imperdiet at vehicula at, bibendum.</p></div>
      <div class="use sep bottom"><h3>Paper</h3><p>Donec quam lacus, imperdiet at vehicula at, bibendum.</p></div>
      <div class="use sep bottom"><h3>Textiles</h3><p>Donec quam lacus, imperdiet at vehicula at, bibendum.</p></div>
    </div>
  </div>
  <div class="contact-head">
    <svg width="30" height="30" viewBox="0 0 30 30"><rect x="4" y="3" width="19" height="24" fill="#fafafa" stroke="#999" transform="rotate(-8 14 15)"/><g stroke="#bbb"><line x1="8" y1="10" x2="19" y2="9"/><line x1="8" y1="14" x2="19" y2="13"/><line x1="8" y1="18" x2="19" y2="17"/></g><line x1="14" y1="23" x2="27" y2="12" stroke="#d9a21b" stroke-width="2.5"/></svg>
    <h2>Contact us</h2>
  </div>
  <form class="contact">
    <label>Name :</label><div class="field"></div>
    <label>Phone :</label><div class="field"></div>
    <label>E-mail :</label><div class="field"></div>
    <label>Message :</label><div class="field msg"></div>
    <div class="submit">SUBMIT</div>
  </form>
  <div class="news">
    <div class="label">
      <svg width="34" height="30" viewBox="0 0 34 30"><rect x="2" y="4" width="30" height="24" fill="#f7f7f7" stroke="#bbb"/><g fill="#c9c9c9"><rect x="6" y="9" width="4" height="15"/><rect x="12" y="9" width="4" height="15"/><rect x="18" y="9" width="4" height="15"/><rect x="24" y="9" width="4" height="15"/></g></svg>
      <h2>Latest News</h2>
    </div>
    <p>Praesent iaculis consectetur pharetra. Ut massa urna, molestie et fermentum pharetra, molestie nec purus. Proin sollicitudin congue tortor, ac blandit ante. Curabitur euismod pretium arcu, sit amet facilisis sapien aliquet molestie. Etiam in odio ut lectus bibendum. &nbsp;&nbsp;<span class="date">July-11-2013</span></p>
    <svg class="next" width="24" height="24" viewBox="0 0 24 24"><circle cx="12" cy="12" r="12" fill="#c4c4c4"/><path d="M10 7l5 5-5 5" fill="none" stroke="#fff" stroke-width="2"/></svg>
  </div>
</div>
<div class="footer-links">Home &nbsp;|&nbsp; About us &nbsp;|&nbsp; Services &nbsp;|&nbsp; Products &nbsp;|&nbsp; News &nbsp;|&nbsp; Contact us</div>
<div class="copyright">Copyright &nbsp;©&nbsp; 2013 &nbsp;www.verdantstemseed.com &nbsp;&nbsp;All rights reserved.</div>
<div class="social">
  <span style="background:#3b5a9a" role="img" aria-label="Social network link"></span>
  <span style="background:#3fa9e0" role="img" aria-label="Social network link"></span>
</div>
</body>
</html>
```